Packaging box design for start up candle company based in Sydney Australia

I need an eye catching box design for my candle company called Morningside Wickery. We specialise only in delicious cake and cocktail scented candles. I want to convey a sense of elegant whimsy.
I have a logo and a style guide which I'm happy with, but need to complete the brand with a stunning box design.
I'd like the same design for two different sized boxes.

```html
<!DOCTYPE html>
<html lang="en">
<head>
<meta charset="utf-8">
<title>Morningside Wickery – Birthday Cake Candle Box</title>
<link rel="stylesheet" href="https://fonts.googleapis.com/css2?family=Cormorant+Garamond:wght@500&family=Barlow:wght@400;500&display=swap">
<style>
  :root {
    --stage: #f2f2f2;
    --paper: #ffffff;
    --paper-shade: #e9e9e9;
    --ink: #141414;
    --ink-soft: #5a5a5a;
    --gold-deep: #a8731f;
    --gold: #d9a03a;
    --gold-light: #f3d27a;
    --gold-line: #dcc08a;
  }
  * { box-sizing: border-box; margin: 0; padding: 0; }
  html, body { width: 1200px; height: 675px; overflow: hidden; }
  body {
    background: var(--stage);
    font-family: "Barlow", sans-serif;
    color: var(--ink);
    position: relative;
  }
  .panel { position: absolute; }
  .panel-top {
    left: 355px; top: 50px; width: 280px; height: 210px;
    background: linear-gradient(120deg, var(--gold-deep) 0%, var(--gold) 35%, var(--gold-light) 60%, var(--gold) 80%, var(--gold-deep) 100%);
    display: flex; align-items: center; justify-content: center;
  }
  .panel-top .brand-name { color: var(--paper); font-size: 17px; }
  .panel-front {
    left: 355px; top: 260px; width: 280px; height: 340px;
    background: var(--paper);
    overflow: hidden;
  }
  .panel-side {
    left: 635px; top: 260px; width: 210px; height: 340px;
    background: var(--paper-shade);
    display: flex; align-items: center; justify-content: center;
    padding: 0 22px;
  }
  .floral {
    position: absolute;
    background: radial-gradient(ellipse at center, rgba(220,192,138,0.45) 0%, rgba(220,192,138,0.12) 60%, rgba(255,255,255,0) 75%);
  }
  .floral-top-left { left: 10px; top: 10px; width: 100px; height: 110px; }
  .floral-top-right { right: 0; top: 40px; width: 110px; height: 120px; }
  .floral-bottom-left { left: 10px; bottom: 20px; width: 100px; height: 120px; }
  .floral-bottom-right { right: 0; bottom: 0; width: 110px; height: 130px; }
  .front-content {
    position: absolute; left: 0; right: 0; top: 118px;
    display: flex; flex-direction: column; align-items: center;
  }
  .brand {
    display: flex; align-items: center; gap: 8px;
  }
  .brand-mark {
    width: 8px; height: 8px; border-radius: 50%;
    background: var(--gold);
  }
  .brand-name {
    font-family: "Cormorant Garamond", serif;
    font-weight: 500;
    font-size: 19px;
    letter-spacing: 2px;
    text-transform: uppercase;
    color: var(--ink);
  }
  .product-type {
    margin-top: 16px;
    width: 170px;
    padding: 2px 0;
    background: linear-gradient(90deg, var(--gold-deep), var(--gold-light), var(--gold));
    color: var(--paper);
    font-size: 9px;
    letter-spacing: 1.8px;
    text-align: center;
    text-transform: uppercase;
  }
  .product-name {
    margin-top: 4px;
    font-weight: 500;
    font-size: 28px;
    line-height: 26px;
    letter-spacing: 5px;
    text-align: center;
    text-transform: uppercase;
  }
  .product-specs {
    margin-top: 44px;
    font-size: 10px;
    letter-spacing: 1.5px;
    line-height: 14px;
    text-align: center;
    text-transform: uppercase;
    color: var(--ink-soft);
  }
  .care-text {
    font-size: 8.5px;
    line-height: 13px;
    letter-spacing: 0.8px;
    text-transform: uppercase;
    color: var(--ink-soft);
  }
</style>
</head>
<body>
  <section class="panel panel-top">
    <span class="brand-name">Morningside Wickery</span>
  </section>

  <section class="panel panel-front">
    <div class="floral floral-top-left" role="img" aria-label="Gold line-art flower illustration"></div>
    <div class="floral floral-top-right" role="img" aria-label="Gold line-art flower illustration"></div>
    <div class="floral floral-bottom-left" role="img" aria-label="Gold line-art flower illustration"></div>
    <div class="floral floral-bottom-right" role="img" aria-label="Gold line-art flower illustration"></div>

    <div class="front-content">
      <div class="brand">
        <span class="brand-mark"></span>
        <span class="brand-name">Morningside Wickery</span>
      </div>
      <div class="product-type">Scented Wax Candle</div>
      <h1 class="product-name">Birthday<br>Cake</h1>
      <p class="product-specs">7oz Glass<br>36hr Burn</p>
    </div>
  </section>

  <section class="panel panel-side">
    <p class="care-text">Hand poured in small batches with a soy wax blend and cotton wick. Trim wick before each burn and never leave a lit candle unattended. Keep away from children, pets and drafts. Burn on a heat safe surface, out of reach.</p>
  </section>
</body>
</html>
```